Real Estate Seller Financing Postcard

I need a postcard that lays out these options contained in the notes that grabs attention, explains the two options easily and is eye-catching. The front needs to have the percentages on it and information about it and on the other side One side exact Text is:
"Monthly income without tenant headaches" in big letters. Also on front "Get
110%
add an "or"
160% of market value for your property. ". The percentages should be displayed and that is not to be a sentence of text. Other side text: I need bullets points for these "Formal protection as a lien holder against home
No commission or closing cost
Fast closings possible
Property taken as is so no repairs.

Add to the top of the back in "It’s simple. I am a new investor without down payment capital who still want to double our portfolio this year to grow our portfolio."
Here are the two options that are to be the largest part of the back
Option 1, you can receive 80% now cash and 30% over a short period of time including interest.

Option 2, where act like a bank allowing you to make 150% if you finance the whole property(ies). No gimmicks and surprises, just simple unconventional financing.

Include Logo Somewhere

Target Market(s)

Property Owners Wanting to Sell Their Property

Industry/Entity Type

Real Estate Investing

Requirements
Must have
• The options promiment and each side with its respective information. Must have logo somewhere
Nice to have
• The options in color other than black.
Should not have
• A picture of money on the front. Any other image is okay.

```html
<!DOCTYPE html>
<html lang="en">
<head>
<meta charset="utf-8">
<title>Seller Financing Postcard</title>
<link href="https://fonts.googleapis.com/css2?family=Roboto+Slab:wght@300;400;500;700&display=swap" rel="stylesheet">
<style>
  :root {
    --stage: #6d6e71;
    --blue: #2b6cb6;
    --teal: #1fb1bf;
    --white: #ffffff;
    --ink-blue: #2f5d9a;
  }
  * { margin: 0; padding: 0; box-sizing: border-box; }
  html, body { width: 894px; height: 1200px; overflow: hidden; }
  body {
    background: var(--stage);
    font-family: "Roboto Slab", Georgia, serif;
    position: relative;
    color: var(--white);
  }
  .postcard {
    position: absolute;
    left: 48px;
    width: 796px;
    overflow: hidden;
    background: var(--white);
  }
  .postcard--front { top: 61px; height: 529px; }
  .postcard--back { top: 620px; height: 527px; }
  .shapes { position: absolute; left: 0; top: 0; width: 796px; }
  .postcard--front .shapes { height: 529px; }
  .postcard--back .shapes { height: 527px; }
  .txt { position: absolute; white-space: nowrap; }

  /* front */
  .headline { left: 32px; top: 70px; font-size: 30px; font-weight: 700; line-height: 1; }
  .subhead { left: 32px; top: 106px; font-size: 21px; font-weight: 500; line-height: 1; }
  .offer-get { left: 32px; top: 164px; font-size: 27px; font-weight: 400; line-height: 1; }
  .offer-rates { left: 32px; top: 207px; font-size: 32px; font-weight: 700; line-height: 1; }
  .offer-rates .or { font-weight: 300; font-style: italic; font-size: 27px; }
  .offer-tail { left: 32px; top: 245px; font-size: 25px; font-weight: 400; line-height: 33px; }
  .benefits {
    right: 20px; top: 423px; list-style: none; text-align: right;
    font-size: 12px; line-height: 23px;
  }
  .benefits li::after {
    content: ""; display: inline-block; width: 7px; height: 7px; border-radius: 50%;
    background: var(--white); margin-left: 9px; vertical-align: 1px;
  }

  .brand {
    position: absolute; display: flex; align-items: center; gap: 7px;
    color: var(--ink-blue); font-size: 13px; font-weight: 500; white-space: nowrap;
  }
  .brand__dot { width: 30px; height: 30px; border: 2px solid var(--ink-blue); border-radius: 50%; }
  .postcard--front .brand { left: 36px; top: 473px; }
  .postcard--back .brand { left: 580px; top: 454px; }

  /* back */
  .intro-title { left: 30px; top: 66px; font-size: 26px; font-weight: 400; line-height: 1; }
  .intro-body { left: 30px; top: 102px; font-size: 22px; font-weight: 300; line-height: 29px; }
  .option-title { font-size: 20px; font-weight: 700; line-height: 1; }
  .option-body { font-size: 16.5px; font-weight: 400; line-height: 23px; }
  .opt1-title { left: 30px; top: 285px; }
  .opt1-body { left: 30px; top: 311px; }
  .opt2-title { left: 30px; top: 407px; }
  .opt2-body { left: 30px; top: 433px; }
</style>
</head>
<body>

<section class="postcard postcard--front">
  <svg class="shapes" viewBox="0 0 796 529">
    <defs>
      <linearGradient id="frontPanel" x1="0" y1="0" x2="0" y2="1">
        <stop offset="0" stop-color="#2b66b3"/>
        <stop offset="1" stop-color="#1eb4c0"/>
      </linearGradient>
      <linearGradient id="meadowPhoto" x1="0" y1="0" x2="0" y2="1">
        <stop offset="0" stop-color="#3f6b2c"/>
        <stop offset="0.5" stop-color="#9fb8a8"/>
        <stop offset="0.62" stop-color="#8fc43c"/>
        <stop offset="1" stop-color="#a8d54a"/>
      </linearGradient>
      <linearGradient id="nightPhoto" x1="0" y1="0" x2="0" y2="1">
        <stop offset="0" stop-color="#1f6a5a"/>
        <stop offset="0.6" stop-color="#1b2a2e"/>
        <stop offset="1" stop-color="#6a4a2e"/>
      </linearGradient>
      <linearGradient id="cornerBand" x1="0" y1="0" x2="1" y2="1">
        <stop offset="0" stop-color="#2a6fb4"/>
        <stop offset="1" stop-color="#1fb6bf"/>
      </linearGradient>
    </defs>
    <rect x="379" y="0" width="417" height="400" fill="url(#meadowPhoto)" role="img" aria-label="Photo of a large timber-framed country house on a green lawn with trees behind"/>
    <polygon points="0,0 379,0 379,268 160,425 0,414" fill="url(#frontPanel)"/>
    <polygon points="392,279 484,332 484,438 392,491 300,438 300,332" fill="var(--blue)"/>
    <polygon points="400,283 485,332 485,430 400,479 315,430 315,332" fill="url(#nightPhoto)" role="img" aria-label="Photo of a small lit cabin at night under a green sky"/>
    <polygon points="458,529 740,329 796,357 796,529" fill="url(#cornerBand)"/>
    <polygon points="306,0 356,0 356,14 331,28 306,14" fill="none" stroke="#2b66b3" stroke-width="1.2"/>
    <polygon points="682,331 708,346 708,376 682,391 656,376 656,346" fill="none" stroke="#ffffff" stroke-width="1.4"/>
    <polygon points="260,485 286,500 286,529 234,529 234,500" fill="none" stroke="#2b66b3" stroke-width="1.2"/>
  </svg>

  <div class="txt headline">MONTHLY INCOME</div>
  <div class="txt subhead">without tenant headaches</div>
  <div class="txt offer-get">Get</div>
  <div class="txt offer-rates">110% <span class="or">or</span> 160%</div>
  <div class="txt offer-tail">of market value<br>for your property</div>

  <ul class="txt benefits">
    <li>No commission or closing cost</li>
    <li>Fast closings possible</li>
    <li>Property taken as is so no repairs</li>
    <li>Formal protection as a lien holder against home</li>
  </ul>

  <div class="brand"><span class="brand__dot"></span>Meridian Real Estate Group</div>
</section>

<section class="postcard postcard--back">
  <svg class="shapes" viewBox="0 0 796 527">
    <defs>
      <linearGradient id="fadedPhoto" x1="0" y1="0" x2="0" y2="1">
        <stop offset="0" stop-color="#f3f3f3"/>
        <stop offset="0.5" stop-color="#dcdcdc"/>
        <stop offset="1" stop-color="#cfcfcf"/>
      </linearGradient>
      <linearGradient id="backPanel" x1="0" y1="0" x2="0" y2="1">
        <stop offset="0" stop-color="#2b66b3"/>
        <stop offset="1" stop-color="#1fa8c0"/>
      </linearGradient>
    </defs>
    <rect x="0" y="0" width="796" height="527" fill="url(#fadedPhoto)" role="img" aria-label="Faded photo of a country house with trees, used as a soft background"/>
    <polygon points="0,0 337,0 494,383 0,383" fill="url(#backPanel)"/>
    <rect x="0" y="383" width="796" height="144" fill="#22b3c2"/>
    <polygon points="0,383 525,383 558,527 0,527" fill="#2b66b3"/>
    <rect x="558" y="435" width="238" height="67" fill="#ffffff"/>
    <rect x="676" y="37" width="84" height="84" fill="#efefef" stroke="#9a9a9a" stroke-width="8"/>
    <rect x="470" y="192" width="326" height="7" fill="#9a9a9a"/>
    <rect x="488" y="237" width="308" height="7" fill="#9a9a9a"/>
    <rect x="506" y="280" width="290" height="7" fill="#9a9a9a"/>
    <rect x="524" y="324" width="272" height="7" fill="#9a9a9a"/>
  </svg>

  <div class="txt intro-title">IT’S SIMPLE.</div>
  <div class="txt intro-body">I am a new investor<br>without down payment<br>capital who still want to double<br>our portfolio this year<br>to grow our portfolio</div>

  <div class="txt option-title opt1-title">OPTION 1</div>
  <div class="txt option-body opt1-body">you can receive 80% now cash and 30%<br>over a short period of time including interest.</div>

  <div class="txt option-title opt2-title">OPTION 2</div>
  <div class="txt option-body opt2-body">where act like a bank allowing you to make 150%<br>if you finance the whole property(ies). No gimmicks<br>and surprises, just simple unconventional financing.</div>

  <div class="brand"><span class="brand__dot"></span>Meridian Real Estate Group</div>
</section>

</body>
</html>
```